<作成物>
■リッチメッセージ
リッチメニュー
合計2枚

〈リッチメニューの項目〉
下の段左から右へ①〜③
下の段左から右へ④〜⑤

〈リッチメニューの表示名〉
①ホームページ ②メニュー   ③SNS
④お客様の声  ⑤スタッフ・店 ⑥予約

デザイン重視でここの表示名はデザイン的に英語の方がよければ
英語でも大丈夫です。意味がわかって
ニュアンスがあっていれば文字を短くするのも
お任せします。あくまでデザイン重視です。

〈画像はこちらから〉

画像
https://47.kovaload.zz/0922-ab73c1d0e5f2a4b6c8d9e0f1a2b3c4d5e6

ロゴ
https://61.kovaload.zz/0922-3d91f7a2c4b6e8d0f1a3c5e7b9d2f4a6c8

※こちらの作成以外に勝手に使用された場合は
著作権侵害で法的手段をとらせていただきます。
作成事例にもしようしないでください。

<サイズ>
・リッチメッセージ(1040×1040ピクセル)
・リッチメニュー(1200×810ピクセル)

<納品形式>
・ai形式(イラストレーターデータ)
・JPG
<詳細>
※添付ファイルをご確認ください。

<備考>
ブランディング効果を期待しています。
どんどん何個でも応募ください。

```html
<!DOCTYPE html>
<html lang="ja">
<head>
<meta charset="utf-8">
<title>凛花サロン リッチメニュー</title>
<link rel="stylesheet" href="https://fonts.googleapis.com/css2?family=Noto+Sans+JP:wght@400;500;700&family=Noto+Serif+JP:wght@600&display=swap">
<style>
  :root {
    --bg-dark: #2a1610;
    --tile-bg: #2f1a12;
    --gold: #c9a06a;
    --gold-soft: #b58a58;
    --text-light: #f3ece4;
    --photo-warm: #c89a76;
    --photo-deep: #5a3424;
    --photo-light: #e9d3bd;
  }
  * { margin: 0; padding: 0; box-sizing: border-box; }
  html, body { width: 717px; height: 1200px; overflow: hidden; background: var(--bg-dark); }
  .menu-canvas { position: relative; width: 717px; height: 1200px; background: var(--bg-dark); }

  .hero {
    position: absolute; left: 0; top: 0; width: 717px; height: 700px;
    background:
      radial-gradient(ellipse at 70% 18%, var(--photo-light) 0%, transparent 45%),
      radial-gradient(ellipse at 30% 70%, #8a5a40 0%, transparent 55%),
      linear-gradient(180deg, var(--photo-warm) 0%, #a8755a 40%, var(--photo-deep) 100%);
  }
  .hero-shade {
    position: absolute; left: 0; top: 270px; width: 717px; height: 140px;
    background: linear-gradient(180deg, transparent, rgba(30,15,10,.35) 50%, transparent);
  }
  .headline {
    position: absolute; left: 0; top: 296px; width: 717px; text-align: center;
    font-family: "Noto Sans JP", sans-serif; font-weight: 400; font-size: 45px; line-height: 58px;
    color: #fff; letter-spacing: 0.5px;
    text-shadow: 0 2px 6px rgba(0,0,0,.75);
  }
  .brand {
    position: absolute; left: 28px; top: 616px;
    font-family: "Noto Serif JP", serif; font-weight: 600; color: var(--gold);
  }
  .brand-name { font-size: 34px; line-height: 42px; letter-spacing: 3px; }
  .brand-sub { font-size: 13px; line-height: 18px; letter-spacing: 3px; }

  .tile-grid {
    position: absolute; left: 10px; top: 714px; width: 697px;
    display: grid; grid-template-columns: repeat(3, 1fr); grid-template-rows: repeat(2, 236px);
    gap: 10px;
  }
  .tile {
    background: var(--tile-bg); border: 1.5px solid var(--gold-soft);
    display: flex; flex-direction: column; align-items: center; justify-content: flex-start;
    padding-top: 44px;
  }
  .tile svg { width: 92px; height: 92px; fill: none; stroke: var(--gold); stroke-width: 3.5; stroke-linejoin: round; stroke-linecap: round; }
  .tile-label { margin-top: 22px; font-family: "Noto Sans JP", sans-serif; font-weight: 500; font-size: 19px; color: var(--text-light); white-space: nowrap; }
  .tile-en { margin-top: 2px; font-family: "Noto Serif JP", serif; font-weight: 600; font-size: 17px; color: var(--text-light); }
</style>
</head>
<body>
<main class="menu-canvas">
  <section class="hero" role="img" aria-label="施術ベッドでリラックスしてマッサージを受ける女性と、花とタオルが置かれた個室のトリートメントベッドの写真"></section>
  <div class="hero-shade"></div>
  <h1 class="headline">完全個室の特別空間を提供する<br>プライベートエステサロン</h1>
  <div class="brand">
    <div class="brand-name">凛花サロン</div>
    <div class="brand-sub">RINKA SALON</div>
  </div>

  <nav class="tile-grid">
    <div class="tile">
      <svg viewBox="0 0 100 100"><path d="M10 50 L50 14 L90 50"/><path d="M22 42 V88 H78 V42"/><path d="M42 88 V62 H58 V88"/></svg>
      <div class="tile-label">ホームページ</div><div class="tile-en">Homepage</div>
    </div>
    <div class="tile">
      <svg viewBox="0 0 100 100"><rect x="28" y="14" width="54" height="68"/><path d="M18 24 V92 H70"/><path d="M38 32 H72 M38 44 H72 M38 56 H72 M38 68 H62"/></svg>
      <div class="tile-label">メニュー</div><div class="tile-en">Menu</div>
    </div>
    <div class="tile">
      <svg viewBox="0 0 100 100"><rect x="12" y="46" width="16" height="42"/><path d="M28 50 L44 34 L50 14 Q60 14 58 30 L56 42 H82 Q90 44 86 54 Q90 60 84 66 Q88 72 80 78 Q82 88 72 88 H28"/></svg>
      <div class="tile-label">最新情報</div><div class="tile-en">SNS</div>
    </div>
    <div class="tile">
      <svg viewBox="0 0 100 100"><path d="M8 16 H62 V52 H30 L18 64 V52 H8 Z"/><path d="M18 28 H52 M18 40 H44"/><path d="M68 36 H92 V70 H84 V82 L72 70 H40 V60"/></svg>
      <div class="tile-label">お客様の声</div><div class="tile-en">Review</div>
    </div>
    <div class="tile">
      <svg viewBox="0 0 100 100"><circle cx="50" cy="34" r="18"/><path d="M18 90 Q18 60 50 58 Q82 60 82 90 Z"/><path d="M50 60 L44 74 L50 82 L56 74 Z"/></svg>
      <div class="tile-label">スタッフ・店舗情報</div><div class="tile-en">Staff &amp; Salon</div>
    </div>
    <div class="tile">
      <svg viewBox="0 0 100 100"><rect x="10" y="20" width="70" height="62" rx="4"/><path d="M10 36 H80 M26 12 V28 M64 12 V28"/><path d="M20 48 H30 M38 48 H48 M20 62 H30 M38 62 H48"/><circle cx="74" cy="74" r="16" fill="var(--tile-bg)"/><path d="M74 64 V74 H82"/></svg>
      <div class="tile-label">ご予約はこちらから</div><div class="tile-en">Reserve</div>
    </div>
  </nav>
</main>
</body>
</html>
```